would like to incorporate logo. having business card done also. a scan code to bring patients to my website would also be great. MarcoTellerDDS.net is web site (this may be something I have to add at printing step, not sure how all that works, so don't sweat this detail)

Logo (maybe on top or upper corner)
Brightwell Crest Dental Associates (probably not necessary because it is written in logo)
Marco Teller DDS

Ossining, NY 10562
555-302-7718
(and second office)

482 N Larchmere Ave
Mt. Kisco, NY 10549
555-604-1293

Reason: partner out of town, want him to see designs to help choose

Reason: almost done choosing. just need a couple more days!!

Reason: finalizing both card and letterhead

Target Market(s)

Wealthy suburb of New York City. business executives, and their home maker wives, and families. Actors and actresses, or stage performers looking for high end cosmetic and implant dentistry, as well as family dentistry.

Industry/Entity Type

Business

Font styles to use
Serif
Script
Other font styles liked:
• open to suggestions

Colors
d3a5cc
acd037
cbdf83
b768aa

Requirements
Nice to have
• can mention fact that we have a private in house lab, so we oversee all aspects of cosmetic procedures

```html
<!DOCTYPE html>
<html lang="en">
<head>
<meta charset="utf-8">
<title>Brightwell Crest Dental Associates — Letterhead</title>
<link rel="stylesheet" href="https://fonts.googleapis.com/css2?family=Libre+Baskerville&family=Didact+Gothic&display=swap">
<style>
  :root {
    --backdrop: #7a7a7a;
    --paper: #ffffff;
    --plum-deep: #4f1f4c;
    --plum-bright: #9c2378;
    --leaf: #5ba847;
    --ink-light: #ffffff;
  }
  * { margin: 0; padding: 0; box-sizing: border-box; }
  html, body {
    width: 1200px; height: 1000px; overflow: hidden;
    background: var(--backdrop);
  }
  .letterhead {
    position: absolute; left: 230px; top: 48px;
    width: 707px; height: 915px;
    background: var(--paper);
    overflow: hidden;
  }
  .header-band { position: absolute; left: 0; top: 0; }
  .brand {
    position: absolute; left: 44px; top: 24px;
    display: flex; align-items: center; gap: 9px;
  }
  .brand-square {
    width: 34px; height: 34px; background: var(--plum-bright); flex: none;
  }
  .brand-name {
    font-family: "Libre Baskerville", Georgia, serif;
    font-size: 17px; line-height: 19px; color: var(--plum-bright);
    white-space: nowrap;
  }
  .address {
    position: absolute; right: 186px; top: 9px;
    font-family: "Didact Gothic", Arial, sans-serif;
    font-size: 10px; line-height: 11.5px;
    color: var(--ink-light); text-align: right;
    font-style: normal;
  }
  .divider {
    position: absolute; left: 529px; top: 18px;
    width: 1px; height: 36px; background: var(--ink-light);
  }
  .contact-list {
    position: absolute; left: 536px; top: 17px;
    list-style: none;
    font-family: "Didact Gothic", Arial, sans-serif;
    font-size: 11px; line-height: 13px; color: var(--ink-light);
  }
  .contact-list li { display: flex; align-items: center; gap: 4px; }
  .contact-list svg { width: 8px; height: 8px; flex: none; }
  .footer-band { position: absolute; left: 0; bottom: 0; }
</style>
</head>
<body>
  <main class="letterhead">
    <svg class="header-band" width="707" height="62" viewBox="0 0 707 62" aria-hidden="true">
      <defs>
        <linearGradient id="plumFade" x1="0" x2="1" y1="0" y2="0">
          <stop offset="0" stop-color="#4f1f4c"/>
          <stop offset="1" stop-color="#9c2378"/>
        </linearGradient>
      </defs>
      <path d="M265 0 H707 V62 H340 C325 30 300 8 265 0 Z" fill="url(#plumFade)"/>
    </svg>

    <div class="brand">
      <span class="brand-square"></span>
      <span class="brand-name">Brightwell Crest<br>Dental Associates</span>
    </div>

    <address class="address">Marco Teller DDS<br>482 N Larchmere Ave<br>Mt. Kisco, NY 10549<br>Ossining, NY 10562</address>
    <span class="divider"></span>
    <ul class="contact-list">
      <li><svg viewBox="0 0 8 8"><rect width="8" height="8" rx="1" fill="#fff"/><path d="M2 2 L3 2 L3.6 3.4 L3 4 Q4 5 4.6 5 L5.2 4.4 L6.4 5 L6.4 6 Q3 6.4 2 2 Z" fill="#6a2260"/></svg>555-302-7718</li>
      <li><svg viewBox="0 0 8 8"><rect width="8" height="8" rx="1" fill="#fff"/><path d="M2 2 L3 2 L3.6 3.4 L3 4 Q4 5 4.6 5 L5.2 4.4 L6.4 5 L6.4 6 Q3 6.4 2 2 Z" fill="#6a2260"/></svg>555-604-1293</li>
      <li><svg viewBox="0 0 8 8"><circle cx="4" cy="4" r="4" fill="#fff"/><circle cx="4" cy="4" r="2.4" fill="none" stroke="#7a2268" stroke-width=".8"/></svg>www.MarcoTellerDDS.net</li>
    </ul>

    <svg class="footer-band" width="707" height="16" viewBox="0 0 707 16" aria-hidden="true">
      <defs>
        <linearGradient id="plumFoot" x1="0" x2="1" y1="0" y2="0">
          <stop offset="0" stop-color="#4f1f4c"/>
          <stop offset="1" stop-color="#9c2378"/>
        </linearGradient>
      </defs>
      <rect x="0" y="0" width="707" height="16" fill="#5ba847"/>
      <path d="M0 0 H538 C546 0 544 10 536 16 H0 Z" fill="url(#plumFoot)"/>
    </svg>
  </main>
</body>
</html>
```